Looking for awesome business card design with attached existing logo

We are a water, mold, and fire damage restoration company called "Torvane Seco" Looking for an awesome business card that is edgy yet professional and unique. Show me what you got!

```html
<!DOCTYPE html>
<html lang="en">
<head>
<meta charset="utf-8">
<title>Torvane Seco – Business Card</title>
<link rel="stylesheet" href="https://fonts.googleapis.com/css2?family=Montserrat:wght@400;500;700;800&display=swap">
<style>
  :root {
    --bg: #d6d9da;
    --navy: #1f3e4c;
    --gold: #d4991f;
    --red: #b52a3c;
    --paper: #f7f7f5;
    --ink: #2b2f33;
  }
  * { box-sizing: border-box; margin: 0; padding: 0; }
  html, body { width: 1200px; height: 905px; overflow: hidden; }
  body {
    background: var(--bg);
    font-family: "Montserrat", Arial, sans-serif;
    position: relative;
  }
  .card {
    position: absolute;
    left: 250px;
    width: 700px;
    height: 400px;
    overflow: hidden;
    box-shadow: 0 10px 24px rgba(0,0,0,0.18);
  }
  .card--front { top: 30px; background: var(--paper); }
  .card--back { top: 475px; background: var(--navy); }

  .brand {
    position: absolute;
    display: flex;
    align-items: center;
    gap: 10px;
    font-weight: 800;
    letter-spacing: 1px;
    text-transform: uppercase;
    line-height: 1;
  }
  .brand__dot { width: 12px; height: 12px; border-radius: 50%; background: var(--gold); flex: none; }
  .card--front .brand { left: 40px; top: 130px; color: var(--navy); font-size: 32px; width: 250px; flex-wrap: wrap; }
  .card--back .brand { left: 0; right: 0; top: 170px; justify-content: center; color: #ffffff; font-size: 54px; }

  .divider {
    position: absolute;
    left: 320px; top: 70px;
    width: 2px; height: 190px;
    background: var(--red);
  }

  .contact { position: absolute; left: 350px; top: 72px; color: var(--ink); }
  .contact__name { font-size: 28px; font-weight: 800; color: var(--navy); letter-spacing: 0.5px; }
  .contact__role { font-size: 16px; margin-top: 4px; }
  .contact__address { font-size: 15px; line-height: 1.4; margin-top: 8px; }
  .contact__list { list-style: none; margin-top: 10px; font-size: 15px; line-height: 1.6; }
  .contact__list li { display: flex; align-items: center; gap: 8px; }
  .contact__list svg { width: 13px; height: 13px; fill: var(--gold); flex: none; }

  .footer-wave { position: absolute; left: 0; bottom: 0; width: 700px; height: 130px; }
  .footer-url {
    position: absolute; right: 40px; bottom: 16px;
    color: #ffffff; font-size: 17px; font-weight: 500; letter-spacing: 0.5px;
  }
</style>
</head>
<body>

<section class="card card--front">
  <div class="brand"><span class="brand__dot"></span><span>Torvane Seco</span></div>
  <div class="divider"></div>

  <div class="contact">
    <p class="contact__name">DALE KINROSS</p>
    <p class="contact__role">CEO/Founder</p>
    <p class="contact__address">Unit 1- 1234 Street Name<br>Country Name, BC</p>
    <ul class="contact__list">
      <li><svg viewBox="0 0 16 16"><path d="M3 1h3l1.5 4-2 1.3a9 9 0 0 0 4.2 4.2L11 8.5l4 1.5v3a2 2 0 0 1-2 2A13 13 0 0 1 1 3a2 2 0 0 1 2-2z"/></svg>604-555-0182</li>
      <li><svg viewBox="0 0 16 16"><path d="M4 0h8a1 1 0 0 1 1 1v14a1 1 0 0 1-1 1H4a1 1 0 0 1-1-1V1a1 1 0 0 1 1-1zm1 2v10h6V2zm3 11a1 1 0 1 0 0 2 1 1 0 0 0 0-2z"/></svg>604-555-0147</li>
      <li><svg viewBox="0 0 16 16"><path d="M0 3h16v1.2L8 9 0 4.2zM0 6l8 4.8L16 6v7H0z"/></svg>info@torvaneseco.com</li>
    </ul>
  </div>

  <svg class="footer-wave" viewBox="0 0 700 130" preserveAspectRatio="none" aria-hidden="true">
    <path d="M0 20 C220 30 440 60 700 130 L0 130 Z" fill="var(--gold)"/>
    <path d="M0 34 C230 42 450 78 700 130 L700 130 L0 130 Z" fill="var(--paper)"/>
    <path d="M0 50 C240 56 460 86 700 100 L700 130 L0 130 Z" fill="var(--navy)"/>
    <path d="M0 28 C240 34 470 70 700 112" fill="none" stroke="var(--gold)" stroke-width="3"/>
  </svg>
  <p class="footer-url">www.torvaneseco.com</p>
</section>

<section class="card card--back">
  <div class="brand"><span class="brand__dot"></span><span>Torvane Seco</span></div>
</section>

</body>
</html>
```